Laundromat washing machine soap instructions poster

I own a laundromat and need a poster explaining to my customers how to load the soap, bleach and fabric softener into our washing machines. I tried to make a poster on canva but it looks terrible. My Laundromat is called "Tidal Lane" and would like my logo to also be on the poster for branding. I would like the poster to use my blue logo colors to match my brand identity.
Under the photo please include the following text:
" *Please place pods inside the washer"
Thanks

```html
<!DOCTYPE html>
<html lang="en">
<head>
<meta charset="utf-8">
<title>Tidal Lane – Where does the soap go?</title>
<link href="https://fonts.googleapis.com/css2?family=Allura&family=Luckiest+Guy&family=Poppins:wght@400;500;700&display=swap" rel="stylesheet">
<style>
  :root {
    --blue-deep: #0f6fc2;
    --blue-mid: #3ea4ee;
    --blue-light: #bfe6fb;
    --navy: #0a1c80;
    --arrow: #4f8cf0;
    --brand-blue: #2a6fb6;
    --ink: #111111;
    --white: #ffffff;
    --headline-shadow: #0d3f8a;
  }
  * { margin: 0; padding: 0; box-sizing: border-box; }
  html, body { width: 951px; height: 1200px; overflow: hidden; background: #ffffff; }
  .poster { position: relative; width: 951px; height: 1200px; overflow: hidden; background: var(--white); font-family: "Poppins", sans-serif; }
  .hero {
    position: absolute; left: 0; top: 0; width: 951px; height: 970px;
    background: linear-gradient(170deg, var(--blue-deep) 0%, #2a8fe0 30%, var(--blue-mid) 55%, #2a8fdc 80%, #1c80d2 100%);
    overflow: hidden;
  }
  .hero__bubbles { position: absolute; inset: 0; }
  .headline__intro {
    position: absolute; left: 66px; top: 66px;
    font-family: "Allura", cursive; font-size: 90px; color: var(--white);
    line-height: 1; white-space: nowrap;
  }
  .headline__main {
    position: absolute; left: 66px; top: 150px; width: 360px;
    font-family: "Luckiest Guy", sans-serif; font-size: 128px; line-height: 0.98;
    font-weight: 400; color: var(--white); white-space: nowrap;
    text-shadow: 5px 5px 0 var(--headline-shadow);
  }
  .dispenser-photo {
    position: absolute; left: 440px; top: 300px; width: 470px; height: 670px;
    border-radius: 18px 18px 0 0;
    background: linear-gradient(180deg, #74787d 0%, #8e9297 45%, #c9ccce 70%, #7a7e83 100%);
  }
  .label {
    position: absolute; background: var(--navy); color: var(--white);
    border-radius: 40px; display: flex; align-items: center; justify-content: center;
    text-align: center; font-weight: 500; line-height: 1.05;
  }
  .label--softener { left: 137px; top: 477px; width: 251px; height: 83px; font-size: 28px; }
  .label--bleach { left: 110px; top: 609px; width: 200px; height: 62px; font-size: 29px; }
  .label--detergent { left: 92px; top: 728px; width: 242px; height: 62px; font-size: 29px; }
  .arrows { position: absolute; inset: 0; pointer-events: none; }
  .footer { position: absolute; left: 0; top: 970px; width: 951px; height: 230px; background: var(--white); }
  .brand { position: absolute; left: 70px; top: 66px; display: flex; align-items: center; gap: 16px; }
  .brand__dot { width: 46px; height: 46px; border-radius: 50%; background: var(--brand-blue); }
  .brand__name { font-weight: 700; font-size: 44px; color: var(--brand-blue); white-space: nowrap; }
  .notice {
    position: absolute; left: 483px; top: 27px; width: 406px; height: 91px;
    border: 2px solid var(--navy); border-radius: 14px;
    display: flex; flex-direction: column; align-items: center; justify-content: center;
    line-height: 1.05;
  }
  .notice__line1 { font-size: 30px; font-weight: 400; color: var(--ink); }
  .notice__line2 { font-size: 30px; font-weight: 700; color: var(--brand-blue); }
  .website {
    position: absolute; left: 483px; top: 130px; width: 406px; text-align: center;
    font-size: 23px; letter-spacing: 4px; color: var(--ink); white-space: nowrap;
  }
  .website__name { color: var(--brand-blue); font-weight: 700; }
</style>
</head>
<body>
<main class="poster">
  <section class="hero">
    <svg class="hero__bubbles" width="951" height="970" viewBox="0 0 951 970" role="img" aria-label="Soft light-blue field of soap bubbles">
      <defs>
        <radialGradient id="bubbleGlow" cx="0.8" cy="0.45" r="0.7">
          <stop offset="0" stop-color="#e6f6ff"/>
          <stop offset="0.5" stop-color="#9fd5f6"/>
          <stop offset="1" stop-color="#3b9de4"/>
        </radialGradient>
      </defs>
      <path d="M795 0 C640 40 520 150 500 300 L520 970 L951 970 L951 0 Z" fill="#d7e3ee"/>
      <path d="M812 0 C660 45 545 160 530 310 L540 970 L951 970 L951 0 Z" fill="url(#bubbleGlow)"/>
    </svg>

    <div class="headline__intro">Where does the</div>
    <h1 class="headline__main">SOAP<br>GO?</h1>

    <div class="dispenser-photo" role="img" aria-label="Photo of an open washing machine detergent dispenser with softener, bleach and detergent compartments"></div>

    <div class="label label--softener">FABRIC<br>SOFTENER</div>
    <div class="label label--bleach">BLEACH</div>
    <div class="label label--detergent">DETERGENT</div>

    <svg class="arrows" width="951" height="970" viewBox="0 0 951 970">
      <defs>
        <marker id="arrowHead" viewBox="0 0 10 10" refX="6" refY="5" markerWidth="3.2" markerHeight="3.2" orient="auto">
          <path d="M0 0 L10 5 L0 10 Z" fill="#4f8cf0"/>
        </marker>
      </defs>
      <g fill="none" stroke="#4f8cf0" stroke-width="9" stroke-linecap="round" marker-end="url(#arrowHead)">
        <path d="M372 525 C430 505 480 550 498 605"/>
        <path d="M300 642 C420 600 560 620 640 702"/>
        <path d="M320 738 C440 700 570 730 640 808"/>
        <path d="M312 776 C380 745 440 770 480 830"/>
      </g>
    </svg>
  </section>

  <footer class="footer">
    <div class="brand">
      <span class="brand__dot"></span>
      <span class="brand__name">Tidal Lane</span>
    </div>
    <div class="notice">
      <span class="notice__line1">PLEASE PLACE PODS</span>
      <span class="notice__line2">INSIDE THE WASHER</span>
    </div>
    <div class="website">www.<span class="website__name">tidallanewash</span>.com</div>
  </footer>
</main>
</body>
</html>
```